home accents e-commerce website

I'd like a professional simple website designed where I can sell my home goods. I already have my domain name registered. I need the website to accept credit card payments and Quenlo. It should have a shopping cart option and calculate sales tax and shipping costs on merchandise automatically.

I'll be taking photographs of the merchandise and writing product descriptions myself. (I'm not a professional photographer, so these photos probably won't look too polished. If you can help me make them look better, that'd be great). As I add new merchandise in the future, I'd like an option where I can log in to the back end myself and add pictures/product descriptions. And take old products down as they sell out. So the website needs to be user-friendly for me, even though I'm completely web design illiterate!

I'd like a creative, talented person who can create a whimsical, cute website. Nothing too corporate-looking.

Thank you!

Target Market(s)

women, online shoppers, New York City-area, (ship products to the United States only)

Industry/Entity Type

Home And Garden

Coding

Coded - Design and coding required

Number of Pages Required

1 page

Font styles to use
Sans Serif

Colors
0355a3
ffffff

Requirements
Must have
• shopping cart feature
• safe, secure credit card and Quenlo payments
• ability for me to go in and add new products and take down old/sold products
Nice to have
• whimsical, cute design
Should not have
• too corporate-looking

```html
<!DOCTYPE html>
<html lang="en">
<head>
<meta charset="utf-8">
<title>Lumora Home Goods</title>
<link href="https://fonts.googleapis.com/css2?family=Montserrat:wght@400;500;600;700&family=Open+Sans:wght@400;600&display=swap" rel="stylesheet">
<style>
:root{
  --brand:#0355a3;
  --accent:#4a85d6;
  --navy:#0d2b4b;
  --navy-line:#1c3f63;
  --ink:#222b33;
  --muted:#8a9099;
  --soft:#f2f2f2;
  --line:#e2e2e2;
  --white:#ffffff;
}
*{box-sizing:border-box;margin:0;padding:0}
html,body{width:1200px;height:2203px;overflow:hidden;background:var(--white)}
body{position:relative;font-family:"Open Sans",sans-serif;color:var(--ink)}
.abs{position:absolute}
.caps{font-family:"Montserrat",sans-serif;text-transform:uppercase;letter-spacing:1.5px}

/* header */
.site-header{left:0;top:0;width:1200px;height:80px;box-shadow:0 2px 6px rgba(0,0,0,.06)}
.brand{left:132px;top:12px;font-family:"Montserrat",sans-serif;font-weight:600;color:var(--brand);line-height:1}
.brand .name{font-size:34px;letter-spacing:1px}
.brand .sub{font-size:12px;letter-spacing:4px;margin-top:4px}
.nav a{position:absolute;top:32px;font-family:"Montserrat",sans-serif;font-size:13px;color:#555;text-decoration:none}
.nav a.active{color:var(--brand);font-weight:600}
.nav a.active:after{content:"";position:absolute;left:-6px;right:-6px;bottom:-14px;height:2px;background:var(--brand)}
.social-dot{top:24px;width:32px;height:32px;border-radius:50%;background:#eef0f2}
.social-dot.on{background:var(--accent)}
.cart-btn{left:968px;top:23px;width:100px;height:33px;border-radius:17px;background:var(--accent);color:var(--white);font-family:"Montserrat",sans-serif;font-size:12px;font-weight:600;display:flex;align-items:center;justify-content:center;gap:6px;letter-spacing:1px}

/* categories */
.categories{left:132px;top:104px;width:228px;height:384px;background:var(--navy)}
.categories .head{height:40px;background:var(--brand);color:var(--white);font-family:"Montserrat",sans-serif;font-size:12px;font-weight:600;letter-spacing:.5px;padding:12px 15px}
.categories li{list-style:none;height:38.4px;border-bottom:1px solid var(--navy-line);color:#d5dde6;font-size:13px;padding:10px 15px;display:flex;justify-content:space-between}
.categories li.active{background:var(--accent);color:var(--white)}
.categories li span{font-size:12px}

/* hero */
.hero{left:385px;top:104px;width:683px;height:384px;background:linear-gradient(135deg,#9ea8ad 0%,#6f7b80 45%,#5b6468 100%)}
.hero-frame{left:538px;top:194px;width:377px;height:189px;border:3px solid var(--white)}
.hero-title{left:538px;top:212px;width:377px;text-align:center;color:var(--white);font-family:"Montserrat",sans-serif;font-weight:600;font-size:36px;line-height:47px;letter-spacing:1px}
.pill{display:flex;align-items:center;justify-content:center;border-radius:20px;font-family:"Montserrat",sans-serif;font-weight:600;font-size:10px;letter-spacing:1px;text-transform:uppercase}
.pill.solid{background:var(--accent);color:var(--white)}
.pill.ghost{border:1px solid var(--white);color:var(--white)}
.pill.outline{border:1.5px solid var(--accent);color:var(--ink);background:var(--white)}

/* promo */
.promo-cell{display:flex;flex-direction:column;align-items:center;justify-content:center;text-align:center}
.promo-cell .label{font-family:"Montserrat",sans-serif;font-size:13px;font-weight:600;letter-spacing:2.5px;color:var(--ink)}
.promo-cell .text{font-size:16px;color:var(--muted);line-height:20px;margin-top:16px}

/* featured */
.featured{left:0;top:1017px;width:1200px;height:562px;background:var(--soft)}
.section-title{font-family:"Montserrat",sans-serif;font-size:19px;font-weight:500;letter-spacing:1.5px;text-align:center;width:1200px;left:0}
.product{width:258px}
.product .photo{width:258px;height:256px}
.product p{font-size:11px;line-height:16px;margin-top:14px;color:#333}
.product .price{font-family:"Montserrat",sans-serif;font-weight:700;font-size:20px;margin-top:12px}
.product .price s{font-weight:400;color:var(--muted);font-size:18px;margin-left:6px}
.icon-btn{width:34px;height:34px;border-radius:50%;border:1px solid var(--line);background:var(--white)}
.arrow-btn{width:32px;height:32px;border-radius:50%;display:flex;align-items:center;justify-content:center}

/* features */
.feature{width:260px;text-align:center}
.feature h4{font-family:"Montserrat",sans-serif;font-size:13px;font-weight:600;letter-spacing:1.5px;margin-top:14px}
.feature hr{width:36px;border:none;border-top:1px solid #cfcfcf;margin:10px auto}
.feature p{font-size:12.5px;color:var(--muted);line-height:17px}
.divider{width:1px;height:169px;border-left:1px dashed #dcdcdc;top:1626px}

/* footer */
.footer{left:0;top:1847px;width:1200px;height:292px;background:var(--soft)}
.foot-head{font-family:"Montserrat",sans-serif;font-size:13px;font-weight:500;letter-spacing:.5px;border-bottom:1px solid var(--line);padding-bottom:18px}
.foot-links div{font-size:12px;color:#666;height:28px}
.email-box{width:280px;height:32px;background:var(--white);font-size:11px;color:#aaa;font-style:italic;padding:9px 14px}
.bottom-bar{left:0;top:2139px;width:1200px;height:64px;background:var(--navy)}
.pay-chip{top:2160px;height:24px;padding:0 6px;background:var(--white);border-radius:3px;font-family:"Montserrat",sans-serif;font-weight:600;font-size:10px;color:var(--brand);display:flex;align-items:center}
</style>
</head>
<body>

<header class="abs site-header">
  <div class="abs brand"><div class="name">lumora</div><div class="sub">HOME GOODS</div></div>
  <nav class="nav">
    <a href="#" class="active" style="left:358px">Home</a>
    <a href="#" style="left:426px">About Lumora</a>
    <a href="#" style="left:539px">How It Work?</a>
    <a href="#" style="left:654px">Contact Us</a>
  </nav>
  <span class="abs social-dot" style="left:773px"></span>
  <span class="abs social-dot on" style="left:811px"></span>
  <span class="abs social-dot" style="left:849px"></span>
  <span class="abs social-dot" style="left:887px"></span>
  <div class="abs cart-btn">
    <svg width="13" height="12" viewBox="0 0 13 12"><path d="M1 3h11l-1.5 8h-8z" fill="none" stroke="#fff" stroke-width="1.5"/><path d="M4 3V1.5h5V3" fill="none" stroke="#fff" stroke-width="1.2"/></svg>CART
  </div>
</header>

<aside class="abs categories">
  <div class="head">ALL CATEGORIES</div>
  <ul>
    <li>Vases<span>»</span></li>
    <li class="active">Throw Pillows<span>»</span></li>
    <li>Blankets and Throws<span>»</span></li>
    <li>For Your Floors<span>»</span></li>
    <li>For Your Walls<span>»</span></li>
    <li>For Your Table<span>»</span></li>
    <li>For Your Bedside<span>»</span></li>
    <li>Let THere Be Light<span>»</span></li>
    <li>Put Your Feet Up<span>»</span></li>
  </ul>
</aside>

<section class="abs hero" role="img" aria-label="Bedroom with patterned grey bedding, white headboard and teal curtains"></section>
<svg class="abs" style="left:405px;top:275px" width="30" height="26" viewBox="0 0 30 26"><path d="M14 2 L2 13 L14 24 V17 H28 V9 H14Z" fill="#fff" opacity=".55"/></svg>
<svg class="abs" style="left:1015px;top:275px" width="30" height="26" viewBox="0 0 30 26"><path d="M16 2 L28 13 L16 24 V17 H2 V9 H16Z" fill="#fff"/></svg>
<div class="abs hero-frame"></div>
<div class="abs hero-title">Blankets<br>And<br>ThrowS</div>
<div class="abs pill solid" style="left:671px;top:369px;width:111px;height:28px">Shop Now</div>

<section>
  <div class="abs" role="img" aria-label="Bed with mint and grey floral comforter set" style="left:156px;top:536px;width:229px;height:216px;background:linear-gradient(135deg,#c8d8d6,#9fb7b4 50%,#7e8c8a)"></div>
  <div class="abs promo-cell" style="left:385px;top:536px;width:228px;height:216px;background:var(--soft)">
    <div class="label">NEW ARRIVAL</div>
    <div class="text">Introducing Lumora<br>Collection</div>
    <div class="pill solid" style="width:111px;height:32px;margin-top:36px">Shop Now</div>
  </div>
  <div class="abs" role="img" aria-label="Bed with crisp white sheets and upholstered headboard" style="left:613px;top:536px;width:431px;height:432px;background:linear-gradient(160deg,#9a9590,#c4c2c4 45%,#8d8c92)"></div>
  <div class="abs promo-cell" style="left:613px;top:660px;width:431px;color:#fff">
    <div class="label" style="color:#fff;font-size:12px;letter-spacing:1.5px">BEST OFFER</div>
    <div style="font-family:Montserrat,sans-serif;font-size:27px;margin-top:8px">Up to <b>70%</b> Off</div>
    <div style="font-family:Montserrat,sans-serif;font-size:15px">Clearance Sale</div>
    <div class="pill ghost" style="width:111px;height:32px;margin-top:36px">Shop Now</div>
  </div>
  <div class="abs promo-cell" style="left:156px;top:752px;width:229px;height:216px;background:var(--soft)">
    <div class="label">BEST SELLER</div>
    <div class="text">Throw Pillows<br>Collection</div>
  </div>
  <div class="abs" role="img" aria-label="Beige damask throw pillows on a sofa" style="left:385px;top:752px;width:228px;height:216px;background:linear-gradient(135deg,#e0d8cc,#c7b9a5 55%,#a99a86)"></div>
</section>

<section class="abs featured"></section>
<h2 class="abs section-title" style="top:1057px">FEATURED PRODUCTS</h2>
<div class="abs arrow-btn" style="left:99px;top:1305px;background:#e9e9e9">
  <svg width="10" height="10" viewBox="0 0 10 10"><path d="M6.5 2 L3.5 5 L6.5 8" fill="none" stroke="#aaa" stroke-width="1.4"/></svg>
</div>
<div class="abs arrow-btn" style="left:1068px;top:1305px;background:var(--accent)">
  <svg width="10" height="10" viewBox="0 0 10 10"><path d="M3.5 2 L6.5 5 L3.5 8" fill="none" stroke="#fff" stroke-width="1.6"/></svg>
</div>
<div class="abs" style="left:460px;top:1109px;width:280px;height:422px;background:var(--white);box-shadow:0 2px 8px rgba(0,0,0,.12)"></div>

<article class="abs product" style="left:167px;top:1122px">
  <div class="photo" role="img" aria-label="Stack of folded woven throw blankets with fringe" style="background:linear-gradient(180deg,#d9d2c6,#b9ad9a 55%,#48556a)"></div>
  <p>It is a long established fact that a reader will be distracted</p>
  <div class="price">$410<s>/ $475</s></div>
  <div class="pill outline" style="width:128px;height:33px;margin-top:18px;font-size:9.5px">Add to cart</div>
</article>
<article class="abs product" style="left:472px;top:1122px">
  <div class="photo" role="img" aria-label="Orange and grey patterned throw pillows" style="background:linear-gradient(135deg,#d96a3a,#a9a39b 50%,#4f4a44)"></div>
  <p>It is a long established fact that a reader will be distracted</p>
  <div class="price">$500</div>
  <div style="display:flex;gap:10px;margin-top:18px;align-items:center">
    <div class="pill solid" style="width:128px;height:33px;font-size:9.5px">Add to cart</div>
    <div class="icon-btn" style="position:relative"><svg class="abs" style="left:10px;top:10px" width="14" height="14" viewBox="0 0 14 14"><path d="M2 12 L12 2 M8 2h4v4 M6 12H2V8" fill="none" stroke="#aaa" stroke-width="1.3"/></svg></div>
    <div class="icon-btn" style="position:relative"><svg class="abs" style="left:10px;top:11px" width="14" height="12" viewBox="0 0 14 12"><path d="M7 11 L1.5 5.5 A3 3 0 0 1 7 2 A3 3 0 0 1 12.5 5.5Z" fill="#aaa"/></svg></div>
  </div>
</article>
<article class="abs product" style="left:776px;top:1122px">
  <div class="photo" role="img" aria-label="Pastel vase with pink roses and a lit candle" style="background:linear-gradient(180deg,#d6dcd8,#e8e4df 50%,#e9c3b6)"></div>
  <p>It is a long established fact that a reader will be distracted</p>
  <div class="price">$540</div>
  <div class="pill outline" style="width:128px;height:33px;margin-top:18px;font-size:9.5px">Add to cart</div>
</article>

<section>
  <div class="abs feature" style="left:84px;top:1652px">
    <svg width="40" height="42" viewBox="0 0 40 42"><path d="M4 18h8v20H4z M14 18 L22 4 c4 0 5 3 4 7 l-2 6h11c3 0 4 3 3 5l-4 14c-1 2-2 2-4 2H14z" fill="#c9c9c9"/></svg>
    <h4>100% GUARANTEE</h4><hr><p>There are many variations of<br>passages of Lorem Ipsum</p>
  </div>
  <div class="abs divider" style="left:339px"></div>
  <div class="abs feature" style="left:339px;top:1652px">
    <svg width="44" height="42" viewBox="0 0 44 42"><path d="M22 4 L38 12 V30 L22 38 L6 30 V12Z M6 12 L22 20 L38 12 M22 20 V38" fill="none" stroke="#c9c9c9" stroke-width="3"/></svg>
    <h4>FREE SHIPPING &amp; RETURN</h4><hr><p>There are many variations of<br>passages of Lorem Ipsum</p>
  </div>
  <div class="abs divider" style="left:599px"></div>
  <div class="abs feature" style="left:599px;top:1652px">
    <svg width="44" height="42" viewBox="0 0 44 42"><path d="M4 22 L16 34 L40 10 L35 5 L16 24 L9 17Z" fill="#c9c9c9"/></svg>
    <h4>10 YEAR WARRANTY</h4><hr><p>There are many variations of<br>passages of Lorem Ipsum</p>
  </div>
  <div class="abs divider" style="left:859px"></div>
  <div class="abs feature" style="left:847px;top:1652px">
    <svg width="44" height="42" viewBox="0 0 44 42"><path d="M6 28 V22 A16 16 0 0 1 38 22 V28" fill="none" stroke="#c9c9c9" stroke-width="4"/><rect x="4" y="24" width="9" height="14" rx="2" fill="#c9c9c9"/><rect x="31" y="24" width="9" height="14" rx="2" fill="#c9c9c9"/></svg>
    <h4>24/7 SUPPORT</h4><hr><p>There are many variations of<br>passages of Lorem Ipsum</p>
  </div>
</section>

<footer class="abs footer"></footer>
<div class="abs foot-head" style="left:156px;top:1893px;width:280px;padding-left:6px">CONTACT US</div>
<div class="abs" style="left:156px;top:1950px">
  <div style="font-size:14px;font-weight:600">Need Help?</div>
  <div style="font-family:Montserrat,sans-serif;font-size:19px;margin-top:10px">Call Us: 555-014-2290</div>
  <div style="font-size:12px;color:#555;margin-top:2px">hello@lumorahome.com</div>
  <div style="font-size:12px;margin-top:14px">Connect with Us:</div>
  <div style="display:flex;gap:7px;margin-top:8px">
    <span style="width:32px;height:32px;border-radius:50%;background:#3b5b9a"></span>
    <span style="width:32px;height:32px;border-radius:50%;background:#3fa2e6"></span>
    <span style="width:32px;height:32px;border-radius:50%;background:#cc2027"></span>
    <span style="width:32px;height:32px;border-radius:50%;background:#4b6f98"></span>
  </div>
</div>
<div class="abs foot-head" style="left:460px;top:1893px;width:280px">CATEGORIES</div>
<div class="abs foot-links" style="left:460px;top:1947px">
  <div style="color:var(--accent);text-decoration:underline">Vases</div><div>Throw Pillows</div><div>Blankets and Throws</div><div>For Your Floors</div><div>For Your Walls</div>
</div>
<div class="abs foot-links" style="left:609px;top:1947px">
  <div>For Your Table</div><div>For Your Bedside</div><div>Let THere Be Light</div><div>Put Your Feet Up</div>
</div>
<div class="abs foot-head" style="left:764px;top:1893px;width:280px">NEWSLETTER</div>
<div class="abs" style="left:764px;top:1947px;width:280px;font-size:12px;color:#555;line-height:16px">Receive email-only deals, special offers and product exclusives</div>
<div class="abs email-box" style="left:764px;top:1994px">Enter Your Email ...</div>
<div class="abs pill solid" style="left:764px;top:2040px;width:100px;height:32px">➤ Send</div>

<div class="abs bottom-bar"></div>
<div class="abs" style="left:156px;top:2163px;font-size:12px;color:#c7d0da">© 2017 Lumora Home Goods. All Rights Reserved.</div>
<div class="abs pay-chip" style="left:763px">Carda</div>
<div class="abs pay-chip" style="left:810px">Paynex</div>
<div class="abs pay-chip" style="left:859px">Orbi</div>
<div class="abs pay-chip" style="left:899px">Quenlo</div>
<div class="abs arrow-btn" style="left:1019px;top:2158px;width:26px;height:26px;background:var(--accent)">
  <svg width="10" height="10" viewBox="0 0 10 10"><path d="M5 8V2 M2 5 L5 2 L8 5" fill="none" stroke="#fff" stroke-width="1.5"/></svg>
</div>

</body>
</html>
```